Faithful in the Small...Powerful together

Capital Campaign for Brightwell Chapel...need it engaging..spiritually based with pics of the community etc...

Target Market(s)

church congregation and sphere of influence

Industry/Entity Type

religious

Colors
EB3D1F
EC4F4E
F09395
F8D3D4
FCEDEE

Requirements
Must have
• tier levels..engaging scripture and photos

```html
<!DOCTYPE html>
<html lang="en">
<head>
<meta charset="utf-8">
<title>Brightwell Chapel – Faithful in the Small, Powerful Together</title>
<link rel="stylesheet" href="https://fonts.googleapis.com/css2?family=Oswald:wght@500;600&family=Roboto+Condensed:wght@700&family=Roboto:wght@400;500;700&display=swap">
<style>
  :root {
    --red: #e31b23;
    --red-deep: #c8141b;
    --ink: #1c1c1c;
    --panel-dark: #141414;
    --white: #ffffff;
    --rule: #cfcfcf;
    --stage: #6f6f6f;
  }
  * { box-sizing: border-box; margin: 0; padding: 0; }
  html, body { width: 1051px; height: 1200px; overflow: hidden; background: var(--stage); }
  body { position: relative; font-family: "Roboto", Arial, sans-serif; color: var(--ink); }

  .spread { position: absolute; left: 0; top: 193px; width: 1051px; height: 813px; overflow: hidden; }

  /* Left panel */
  .panel-left { position: absolute; left: 0; top: 0; width: 526px; height: 813px; }
  .panel-left .backdrop { position: absolute; inset: 0; background: linear-gradient(180deg, #2b2b2b 0%, #1d1d1d 55%, #111 100%); }
  .card { position: absolute; left: 38px; top: 38px; width: 449px; height: 734px; background: var(--white); border-radius: 18px; overflow: hidden; }
  .card-title { position: absolute; top: 36px; width: 100%; text-align: center; font-family: "Roboto Condensed", sans-serif; font-weight: 700; font-size: 24px; color: var(--red); letter-spacing: .2px; }
  .card-intro { position: absolute; top: 64px; left: 0; width: 100%; text-align: center; font-size: 17px; line-height: 22px; color: var(--ink); }

  .tier-table { position: absolute; left: 38px; top: 118px; width: 373px; border-collapse: separate; border-spacing: 0; border: 1px solid var(--rule); border-radius: 6px; overflow: hidden; font-size: 14.5px; }
  .tier-table caption { caption-side: top; background: var(--red); color: var(--white); font-family: "Roboto Condensed", sans-serif; font-weight: 700; font-size: 23px; height: 32px; line-height: 33px; border-radius: 6px 6px 0 0; }
  .tier-table th, .tier-table td { border-right: 1px solid var(--rule); border-bottom: 1px solid var(--rule); text-align: center; }
  .tier-table tr > :last-child { border-right: 0; }
  .tier-table tbody tr:last-child td { border-bottom: 0; }
  .tier-table thead th { height: 40px; font-weight: 700; font-size: 15px; }
  .tier-table tbody td { height: 48.5px; }
  .tier-table td.group { text-align: left; padding-left: 13px; font-size: 13.5px; line-height: 17px; }
  .tier-table .total-label { text-align: right; padding-right: 22px; font-weight: 700; font-size: 17px; }

  .margin-note { position: absolute; left: 38px; top: 450px; font-size: 16.5px; font-weight: 500; }
  .margin-list { position: absolute; left: 38px; top: 480px; list-style: none; font-size: 17px; line-height: 22px; }
  .margin-list li { position: absolute; top: 0; padding-left: 19px; white-space: nowrap; }
  .margin-list li svg { position: absolute; left: 0; top: 4px; }

  .card-footer { position: absolute; left: 5px; top: 565px; width: 439px; height: 164px; background: var(--red); border-radius: 0 0 14px 14px; color: var(--white); }
  .contact-title { position: absolute; left: 31px; top: 27px; font-family: "Roboto Condensed", sans-serif; font-weight: 700; font-size: 18px; text-decoration: underline; text-underline-offset: 3px; }
  .contact-list { position: absolute; left: 31px; top: 56px; list-style: none; font-size: 13.5px; line-height: 17px; }
  .contact-list li { position: relative; padding-left: 25px; margin-bottom: 4px; }
  .contact-list svg { position: absolute; left: 0; top: 2px; }
  .footer-mark { position: absolute; left: 265px; top: 22px; width: 141px; height: 118px; background: var(--white); display: flex; flex-direction: column; align-items: center; justify-content: center; }
  .footer-mark .name { font-family: "Roboto", sans-serif; font-weight: 500; font-size: 24px; color: var(--ink); }
  .footer-mark .sub { font-family: "Roboto", sans-serif; font-weight: 500; font-size: 13px; color: var(--ink); letter-spacing: 1px; }

  /* Right panel */
  .panel-right { position: absolute; left: 526px; top: 0; width: 525px; height: 813px; background: var(--panel-dark); overflow: hidden; }
  .panel-right .backdrop { position: absolute; inset: 0; background: linear-gradient(180deg, #1e1e1e 0%, #151515 60%, #0f0f0f 100%); }
  .brand { position: absolute; top: 112px; left: 0; width: 100%; text-align: center; color: var(--white); font-family: "Roboto", sans-serif; font-weight: 500; }
  .brand .name { display: block; font-size: 40px; line-height: 44px; }
  .brand .sub { display: block; font-size: 21px; letter-spacing: 1.5px; margin-top: 2px; }
  .headline { position: absolute; top: 238px; left: 0; width: 100%; text-align: center; font-family: "Oswald", sans-serif; font-weight: 600; font-size: 43px; line-height: 55px; color: var(--white); text-transform: uppercase; }
  .goal { position: absolute; left: 96px; top: 360px; width: 333px; height: 38px; border-radius: 19px; background: var(--red); text-align: center; font-family: "Oswald", sans-serif; font-weight: 500; font-size: 25px; line-height: 38px; color: var(--ink); }
  .photo-area { position: absolute; left: 0; top: 0; }
</style>
</head>
<body>
<main class="spread">

  <section class="panel-left">
    <div class="backdrop" role="img" aria-label="Darkened photo of a riverside steel bridge"></div>
    <article class="card">
      <h2 class="card-title">REALISTIC PARTICIPATION MODEL</h2>
      <p class="card-intro">Not everyone will give equally—so let’s build<br>a real-world scenario:</p>

      <table class="tier-table">
        <caption>TIERED GIVING PLAN</caption>
        <colgroup><col style="width:95px"><col style="width:72px"><col style="width:106px"><col style="width:100px"></colgroup>
        <thead>
          <tr><th>Group</th><th>People</th><th>Weekly Gift</th><th>Yearly Total</th></tr>
        </thead>
        <tbody>
          <tr><td class="group">Leadership<br>Givers</td><td>10</td><td>$100</td><td>$52,000</td></tr>
          <tr><td class="group">Core Givers</td><td>40</td><td>$40</td><td>$83,200</td></tr>
          <tr><td class="group">Consistent<br>Givers</td><td>60</td><td>$20</td><td>$62,400</td></tr>
          <tr><td class="group">Entry Givers</td><td>40</td><td>$10</td><td>$20,800</td></tr>
          <tr><td class="total-label" colspan="3">Total:</td><td>$218,400</td></tr>
        </tbody>
      </table>

      <p class="margin-note">This exceeds the goal, giving margin for:</p>
      <ul class="margin-list">
        <li style="left:0"><svg width="13" height="13" viewBox="0 0 13 13"><circle cx="6.5" cy="6.5" r="6.5" fill="var(--red)"/><path d="M3.5 6.7l2 2 4-4.2" fill="none" stroke="#fff" stroke-width="1.8"/></svg>Missed<br>weeks</li>
        <li style="left:107px"><svg width="13" height="13" viewBox="0 0 13 13"><circle cx="6.5" cy="6.5" r="6.5" fill="var(--red)"/><path d="M3.5 6.7l2 2 4-4.2" fill="none" stroke="#fff" stroke-width="1.8"/></svg>Lower<br>participation</li>
        <li style="left:239px"><svg width="13" height="13" viewBox="0 0 13 13"><circle cx="6.5" cy="6.5" r="6.5" fill="var(--red)"/><path d="M3.5 6.7l2 2 4-4.2" fill="none" stroke="#fff" stroke-width="1.8"/></svg>Unexpected<br>needs</li>
      </ul>

      <footer class="card-footer">
        <h3 class="contact-title">CONTACT US</h3>
        <ul class="contact-list">
          <li><svg width="14" height="14" viewBox="0 0 14 14"><circle cx="7" cy="7" r="7" fill="#1a1a1a"/><path d="M7 3.2a2.4 2.4 0 0 0-2.4 2.4C4.6 7.5 7 10.6 7 10.6s2.4-3.1 2.4-5A2.4 2.4 0 0 0 7 3.2z" fill="none" stroke="#fff" stroke-width="1"/></svg>1180 Maple Ridge Road<br>Fairhaven, Tennessee 37000</li>
          <li><svg width="14" height="14" viewBox="0 0 14 14"><circle cx="7" cy="7" r="7" fill="#1a1a1a"/><path d="M4.5 3.8l1.4-.3.8 1.8-.9.7a5 5 0 0 0 2.2 2.2l.7-.9 1.8.8-.3 1.4C7 9.8 4.2 7 4.5 3.8z" fill="#fff"/></svg>555.014.2870</li>
          <li><svg width="14" height="14" viewBox="0 0 14 14"><circle cx="7" cy="7" r="7" fill="#1a1a1a"/><g fill="none" stroke="#fff" stroke-width=".9"><circle cx="7" cy="7" r="3.8"/><ellipse cx="7" cy="7" rx="1.7" ry="3.8"/><path d="M3.2 7h7.6"/></g></svg>www.brightwellchapel.org</li>
        </ul>
        <div class="footer-mark"><span class="name">Brightwell</span><span class="sub">CHAPEL</span></div>
      </footer>
    </article>
  </section>

  <section class="panel-right">
    <div class="backdrop" role="img" aria-label="Darkened photo of a riverside bridge at dusk"></div>
    <div class="brand"><span class="name">Brightwell</span><span class="sub">CHAPEL</span></div>
    <h1 class="headline">Faithful in the small,<br>powerful together.</h1>
    <p class="goal">GOAL: $150,000 in 12 Months</p>
    <svg class="photo-area" width="525" height="813" viewBox="0 0 525 813">
      <path d="M18 813 C8 735 40 675 115 660 C165 650 185 615 240 605 C290 596 330 578 360 560 L420 548 C470 528 505 490 525 445 L525 813 Z" fill="var(--red)"/>
      <path role="img" aria-label="Photo of three church volunteers with a shopping cart full of donated supplies" d="M32 813 C24 742 55 690 122 676 C170 666 192 632 245 622 C292 613 332 596 362 578 L424 566 C472 546 507 510 525 470 L525 813 Z" fill="url(#photoTone)"/>
      <defs>
        <linearGradient id="photoTone" x1="0" y1="0" x2="1" y2="1">
          <stop offset="0" stop-color="#8a7266"/>
          <stop offset=".45" stop-color="#6f7f9a"/>
          <stop offset="1" stop-color="#4b4f5c"/>
        </linearGradient>
      </defs>
    </svg>
  </section>

</main>
</body>
</html>
```